Web Design job - Condo Debts Collection Business needs a Web Design

I need a site for a client, who works with condo debts collection, and ensure all revenues provided by condo fees will be always available to the building manager of condo on a specific date, regardless of defaults.
I have the visual identity (logo, slogan and colors) of the company, and some requirements on layout (kind of slider, menu options, phone number on a noble position, etc) - maybe I can do a sketch, but I like the idea of give some freedom to designer.

*** PLEASE, we have no interest in templates. We want something new***

Target Market(s)

I have two targets for this design: - Condominium's building manager. This target is looking for a solution to overdue debts on it's condo. - Residents on condominiums. This target wants to live in a better place, where their neighbors pay their condominium fees on time.

Number of Pages Required

1 page

Requirements
Must have
• - Slider with title, some short text related, a nice image (I prefer happy and/or peaceful family, people doing business, happy friends, and so on).
• - I have a special attention to menu. I'm looking for one I can have a nice effect, more elegant, charming, kind of innovative.
• - Phone number on the top (or clearly visible).
• - Member log in area or icon on the top (or clearly visible).
• - News/articles area.
• - Modern fonts, with good quality, sans-serif on areas where reading is more intensive (prefer Google web-fonts).
• - Colors specified on attached files.
Nice to have
• - Clear background color, cause it's better to read larger texts (like articles). Dark backgrounds makes reading difficult.
• - A site with effects (like shadows, lines, curves, gradients, lights) is usually pretty.
• - I pay attention on beautiful footers.
Should not have
• - Images with a lot of money (I don't sell richness, I sell tranquility, peace, harmony, safety).
• - Poor menu.

```html
<!DOCTYPE html>
<html lang="en">
<head>
<meta charset="utf-8">
<title>Condara – Condo Living</title>
<link href="https://fonts.googleapis.com/css2?family=Playfair+Display:wght@400;700;900&display=swap" rel="stylesheet">
<style>
:root{
  --yellow:#e3c43a;
  --yellow-deep:#d9b92e;
  --purple:#1e0a4a;
  --white:#ffffff;
}
*{margin:0;padding:0;box-sizing:border-box}
html,body{width:1200px;height:1200px;overflow:hidden;background:var(--white)}
body{position:relative;font-family:'Playfair Display',serif;color:var(--purple)}
.abs{position:absolute}
.hero-photo{left:0;top:0;width:1200px;height:575px;
  background:linear-gradient(100deg,#d9c7a8 0%,#e6d2ae 22%,#c7cbbf 40%,#a9bcb6 60%,#8fa7a6 78%,#7d8f8c 100%);}
.hero-haze{left:0;top:0;width:1200px;height:575px;background:linear-gradient(180deg,rgba(255,255,255,.15),rgba(255,255,255,0) 40%,rgba(240,225,200,.35))}
.topbar{left:230px;top:0;width:970px;height:64px;background:var(--yellow);clip-path:polygon(0 0,100% 0,100% 100%,40px 100%)}
.call{left:311px;top:14px;color:var(--white);font-weight:700;font-size:16px;line-height:20px}
.call .phone{font-size:17px;letter-spacing:1.5px}
.slash{left:474px;top:9px}
.brand{left:48px;top:40px;display:flex;align-items:center;gap:10px;color:var(--yellow);font-weight:700;font-size:34px}
.brand .mark{width:22px;height:22px;background:var(--yellow)}
.nav{left:476px;top:90px;font-weight:700;font-size:16px;color:var(--white)}
.nav a{color:inherit;text-decoration:none;position:absolute;white-space:nowrap}
.login{left:1010px;top:82px;width:131px;height:39px;background:var(--yellow);color:var(--white);font-weight:700;font-size:16px;display:flex;align-items:center;justify-content:center}
.headline{left:100px;top:222px;font-weight:700;font-size:73px;line-height:86px;color:var(--purple);letter-spacing:.3px}
.arrow-box{top:311px;width:86px;height:47px;background:var(--white);display:flex;align-items:center;justify-content:center}
.btn-read{left:97px;top:411px;width:210px;height:48px;background:var(--yellow);color:var(--white);font-size:30px;display:flex;align-items:center;justify-content:center}
.offers{left:325px;top:416px;width:189px;text-align:center;font-size:30px;color:var(--purple);padding-bottom:4px;border-bottom:4px solid var(--yellow)}
.intro-card{left:97px;top:490px;width:246px;height:390px;background:var(--purple);color:var(--white);padding:26px 24px 26px 31px;box-shadow:0 8px 10px rgba(30,10,74,.35)}
.intro-card h2{font-size:34px;line-height:43px;font-weight:700}
.intro-card p{margin-top:20px;font-size:15px;line-height:28px;font-weight:700}
.btn-all{position:absolute;left:33px;top:322px;width:180px;height:40px;background:var(--white);color:var(--purple);border-radius:8px;font-weight:900;font-size:22px;display:flex;align-items:center;justify-content:center}
.service-card{top:557px;width:246px;height:327px;background:var(--purple);box-shadow:0 8px 10px rgba(30,10,74,.35);overflow:hidden}
.service-card .thumb{height:159px}
.service-card p{padding:18px 10px 0 40px;color:var(--white);font-size:12.8px;line-height:28px;font-weight:700}
.divider{left:0;top:925px;width:1200px;height:6px;background:#e6e6e6}
.projects{left:0;top:931px;width:1200px;height:269px;background:linear-gradient(180deg,var(--yellow),var(--yellow-deep))}
.tabs{left:73px;top:1012px;width:1054px;font-size:31px;font-weight:700;color:var(--purple)}
.tabs span{position:absolute;top:-16px;white-space:nowrap}
.tab-line{left:73px;top:1044px;width:1054px;height:3px;background:var(--white)}
.project-thumb{top:1083px;width:245px;height:117px;box-shadow:0 4px 8px rgba(0,0,0,.2)}
</style>
</head>
<body>
<div class="abs hero-photo" role="img" aria-label="Smiling man sitting on a wall above a sunny beach and bay"></div>
<div class="abs hero-haze"></div>

<div class="abs topbar"></div>
<div class="abs call">Call Us Now<br><span class="phone">1-800-555-0147</span></div>
<svg class="abs slash" width="46" height="46" viewBox="0 0 46 46"><polygon points="0,0 16,0 46,46 30,46" fill="#fff"/></svg>

<div class="abs brand"><span class="mark"></span>Condara</div>

<nav class="abs nav">
  <a style="left:0">Home</a>
  <a style="left:74px">Services</a>
  <a style="left:170px">Reports</a>
  <a style="left:259px">Testimonials</a>
  <a style="left:384px">Blog</a>
  <a style="left:449px">Contact</a>
</nav>
<div class="abs login">Members Login</div>

<h1 class="abs headline">Why living in a Condo<br>is a good Choice</h1>

<div class="abs arrow-box" style="left:0">
  <svg width="70" height="20" viewBox="0 0 70 20"><line x1="6" y1="10" x2="68" y2="10" stroke="#e3c43a" stroke-width="3"/><polyline points="18,2 6,10 18,18" fill="none" stroke="#e3c43a" stroke-width="3"/></svg>
</div>
<div class="abs arrow-box" style="left:1114px">
  <svg width="70" height="20" viewBox="0 0 70 20"><line x1="2" y1="10" x2="64" y2="10" stroke="#e3c43a" stroke-width="3"/><polyline points="52,2 64,10 52,18" fill="none" stroke="#e3c43a" stroke-width="3"/></svg>
</div>

<div class="abs btn-read">Read More</div>
<div class="abs offers">Our Offers</div>

<section class="abs intro-card">
  <h2>We are Speclaized</h2>
  <p>Condara a solid reputation for delivering exceptional architectural and interior design services to private sector, and industrial clients.</p>
  <div class="btn-all">Read All</div>
</section>

<article class="abs service-card" style="left:370px">
  <div class="thumb" role="img" aria-label="Modern two-storey house with a green lawn" style="background:linear-gradient(180deg,#c9d4da 0%,#b7bcbe 55%,#6f9a48 100%)"></div>
  <p>Architecture is our passion, turning ideas into reality and giving buildings a timeless footprint in a community are the values Condara was built on.</p>
</article>
<article class="abs service-card" style="left:640px">
  <div class="thumb" role="img" aria-label="Bright bedroom with a wooden wall and white bed" style="background:linear-gradient(90deg,#7a5a3e 0%,#9c7a5a 35%,#e6e2dc 60%,#d8d2c8 100%)"></div>
  <p>Architecture is our passion, turning ideas into reality and giving buildings a timeless footprint in a community are the values Condara was built on.</p>
</article>
<article class="abs service-card" style="left:913px">
  <div class="thumb" role="img" aria-label="Coastal shoreline with a bridge in the distance" style="background:linear-gradient(180deg,#b9cbd8 0%,#9aa9b4 45%,#6d7a80 70%,#c7c2b6 100%)"></div>
  <p>Architecture is our passion, turning ideas into reality and giving buildings a timeless footprint in a community are the values Condara was built on.</p>
</article>

<div class="abs divider"></div>
<section class="abs projects"></section>
<div class="abs tabs">
  <span style="left:16px">All Projects</span>
  <span style="left:219px">Houses</span>
  <span style="left:354px">Decoration</span>
  <span style="left:557px">Furniture</span>
</div>
<div class="abs tab-line"></div>

<div class="abs project-thumb" style="left:67px;background:linear-gradient(180deg,#f2f2f2,#cfcfcf)" role="img" aria-label="White gallery interior with skylights"></div>
<div class="abs project-thumb" style="left:341px;background:linear-gradient(180deg,#c9dbe8 0%,#b5c3cc 50%,#8a7f6c 100%)" role="img" aria-label="Traditional castle on a stone wall"></div>
<div class="abs project-thumb" style="left:613px;background:linear-gradient(180deg,#eef2ef 0%,#9fb59a 50%,#3c3f3e 100%)" role="img" aria-label="Low modern house among trees"></div>
<div class="abs project-thumb" style="left:888px;background:linear-gradient(180deg,#d9d0c6 0%,#a35a34 45%,#cfc3b4 100%)" role="img" aria-label="House with a wooden pergola terrace"></div>
</body>
</html>
```